Higher $ Now Guaranteed! Redesign Web Page(s) Style Composition and Color (Graphics design-not code)

We need a modern look for an existing website. You can either use or change the current logo. Choice of colors, fonts, style is up to you. Sample URLs and additional details are provided in the attached document. Most of our struggle has been the appearance of the directory listings (city) page.
----------------------------------------------------------------------------------
--> Increased Project Budget and Now Funds are GUARANTEED
--> Added an additional attachment in response to questions
-->THIS PROJECT IS FOR GRAPHICS/DESIGN NOT CODE
The project is mostly a few areas of text and colored boxes or lines. Hopefully a skilled designer can place these elements in an attractive layout and choose the right colors and styles. There are no complex drawings required for this project.

*** We are involved with other projects from time to time and expect that the winning designer will be given the first opportunity at this future work. ***

*** There is no requirement to do any code but if you submit a design feel free to indicate if you wish to be considered for any future code work on this site or others ***

Font styles to use
Sans Serif

Requirements
Must have
• Rounded corners on images and buttons with nice gradients or hover effects.
Nice to have
• Attached an additional descriptions document to help with these answers.
Should not have
• Small fonts, traditional older looking rectangular buttons, dull or boring color schemes

```html
<!DOCTYPE html>
<html lang="en">
<head>
<meta charset="utf-8">
<title>LocateTaxPros — City Directory</title>
<link href="https://fonts.googleapis.com/css2?family=Raleway:wght@400;500;700&display=swap" rel="stylesheet">
<style>
:root{
  --page:#f7f7f7;
  --ink:#3d4e5a;
  --muted:#5a5a5a;
  --rule:#dcdcdc;
  --panel:#ececec;
  --white:#ffffff;
  --yellow:#f2b115;
  --yellow-btn:#c38f10;
  --navy:#172731;
  --green:#7dc242;
  --teal:#37bd9b;
  --teal-btn:#2b9a7d;
  --cyan:#50c4ca;
  --cyan-btn:#3a9ea3;
  --orange:#f07a1a;
}
*{box-sizing:border-box;margin:0;padding:0}
html,body{width:1200px;height:690px;overflow:hidden}
body{background:var(--page);font-family:"Raleway",sans-serif;color:var(--ink);position:relative}
.abs{position:absolute}

.brand{left:86px;top:24px;display:flex;align-items:center;gap:8px;font-size:22px;font-weight:700;color:var(--ink)}
.brand-dot{width:14px;height:14px;border-radius:50%;background:var(--ink)}
.nav{left:517px;top:38px;display:flex;gap:47px;font-size:13.5px;letter-spacing:.3px;color:var(--ink)}
.nav-search{left:860px;top:39px}
.nav-divider{left:912px;top:34px;width:1px;height:26px;background:var(--rule)}
.phone{left:948px;top:33px;display:flex;align-items:center;gap:10px;font-size:20px;font-weight:500;color:var(--ink)}
.header-rule{left:86px;top:91px;width:1029px;height:1px;background:var(--rule)}

.directory{left:86px;top:127px;width:524px;height:395px;background:var(--panel);border-radius:4px}
.city-select{left:15px;top:15px;width:495px;height:53px;background:var(--white);border-radius:4px;display:flex;align-items:center;padding:0 18px;gap:14px;font-size:13px;color:var(--ink)}
.city-select .caret{margin-left:auto}
.listing{width:241px;height:141px;background:var(--white);border-radius:4px;overflow:hidden}
.listing-head{height:55px;display:flex;align-items:center;justify-content:center;text-align:center;color:var(--white);font-weight:700;font-size:15.5px;line-height:19px;padding:0 20px}
.listing-body{padding-top:12px;text-align:center;font-size:13px;line-height:16px;color:var(--muted)}
.head-yellow{background:var(--yellow)}
.head-navy{background:var(--navy)}
.head-green{background:var(--green)}
.cta-list{background:var(--teal);border-radius:4px;width:241px;height:141px;color:var(--white);text-align:center}
.cta-list h2{font-size:23px;font-weight:700;margin-top:38px}
.btn{display:inline-flex;align-items:center;justify-content:center;height:32px;width:181px;border-radius:3px;color:var(--white);font-size:11px;font-weight:700;letter-spacing:.3px}
.btn-teal{background:var(--teal-btn);margin-top:13px}

.promo{border-radius:4px;overflow:hidden;display:flex;color:var(--white)}
.promo-photo{width:176px;height:100%}
.promo-copy{flex:1;padding:17px 18px 0}
.promo-copy h3{font-size:16px;font-weight:700;line-height:20px}
.promo-copy p{font-size:13px;line-height:16px;margin-top:6px}
.promo-preparer{left:629px;top:127px;width:485px;height:186px;background:var(--yellow)}
.photo-writing{background:linear-gradient(135deg,#c96a2a 0%,#e8c8a6 45%,#3d4b5c 100%)}
.btn-yellow{background:var(--yellow-btn);margin-top:17px}
.promo-firm{left:630px;top:335px;width:484px;height:187px;background:var(--cyan)}
.photo-paperwork{background:linear-gradient(135deg,#e9eaec 0%,#c9a27c 55%,#8e4a22 100%)}
.btn-cyan{background:var(--cyan-btn);margin-top:15px}

.footer{left:0;top:565px;width:1200px;height:125px;background:var(--navy);color:var(--white)}
.footer-links{left:86px;top:39px;display:flex;gap:22px;font-size:13.5px;align-items:center}
.footer-links .current{color:var(--orange)}
.social{display:flex;gap:12px;margin-left:6px}
.social span{width:13px;height:13px;border-radius:50%;background:var(--white)}
.legal{left:86px;top:73px;font-size:13px;display:flex;gap:16px}
.footer-brand{left:974px;top:46px;display:flex;align-items:center;gap:8px;font-size:20px;font-weight:700}
.footer-brand .brand-dot{background:var(--white)}
</style>
</head>
<body>
<header>
  <div class="abs brand"><span class="brand-dot"></span>LocateTaxPros</div>
  <nav class="abs nav"><span>HOME</span><span>GET LISTED</span><span>CONTACT US</span></nav>
  <svg class="abs nav-search" width="15" height="15" viewBox="0 0 15 15"><circle cx="6" cy="6" r="4.8" fill="none" stroke="#3d4e5a" stroke-width="1.6"/><line x1="9.5" y1="9.5" x2="13.5" y2="13.5" stroke="#3d4e5a" stroke-width="1.8" stroke-linecap="round"/></svg>
  <div class="abs nav-divider"></div>
  <div class="abs phone">
    <svg width="22" height="22" viewBox="0 0 24 24"><path d="M6.6 2.5l3 3.6-2 2.4c1.2 2.8 3.4 5 6.2 6.2l2.4-2 3.6 3-1.8 3.2C11 19 4.9 12.9 3.3 5z" fill="#3d4e5a"/><path d="M14 3a7 7 0 0 1 7 7M14 6.5a3.5 3.5 0 0 1 3.5 3.5" stroke="#3d4e5a" stroke-width="1.8" fill="none" stroke-linecap="round"/></svg>
    555-201-4730
  </div>
  <div class="abs header-rule"></div>
</header>

<main>
  <section class="abs directory">
    <div class="abs city-select">
      <svg width="15" height="15" viewBox="0 0 15 15"><circle cx="6" cy="6" r="4.8" fill="none" stroke="#3d4e5a" stroke-width="1.6"/><line x1="9.5" y1="9.5" x2="13.5" y2="13.5" stroke="#3d4e5a" stroke-width="1.8" stroke-linecap="round"/></svg>
      SELECT CITY
      <svg class="caret" width="16" height="9" viewBox="0 0 16 9"><path d="M0 0h16L8 9z" fill="#8a9aa5"/></svg>
    </div>
    <article class="abs listing" style="left:15px;top:81px">
      <div class="listing-head head-yellow">HARBOR LANE TAX SERVICE</div>
      <div class="listing-body">48 Alder Rd,<br>WA 98010<br>Phone: (555) 014-2277</div>
    </article>
    <article class="abs listing" style="left:269px;top:81px">
      <div class="listing-head head-navy">QM TAX SERVICE</div>
      <div class="listing-body">207 Birch St,<br>WA 98010<br>Phone: (555) 014-2277</div>
    </article>
    <article class="abs listing" style="left:15px;top:235px">
      <div class="listing-head head-green">MARLOW DANA K<br>CPA</div>
      <div class="listing-body">31 W Pond St Ste 104,<br>WA 98010<br>Phone: (555) 014-2277</div>
    </article>
    <div class="abs cta-list" style="left:269px;top:235px">
      <h2>LIST YOUR FIRM</h2>
      <span class="btn btn-teal">GET REGISTER</span>
    </div>
  </section>

  <section class="abs promo promo-preparer">
    <div class="promo-photo photo-writing" role="img" aria-label="Photo of a hand signing a document with a pen"></div>
    <div class="promo-copy">
      <h3>ARE YOU A TAX PREPARER?</h3>
      <p>Our directories of tax professionals give you immediate access to new clients and prospects looking for income tax preparation and tax services in your local area.</p>
      <span class="btn btn-yellow">SUBMIT LISTING</span>
    </div>
  </section>

  <section class="abs promo promo-firm">
    <div class="promo-copy">
      <h3>HAVE A LOCAL TAX FIRM<br>CONTACT ME</h3>
      <p>Our directories of tax professionals give you immediate access to the very best tax preparers and income tax advisors in your area.</p>
      <span class="btn btn-cyan">GET STARTED</span>
    </div>
    <div class="promo-photo photo-paperwork" role="img" aria-label="Photo of hands filling in tax forms beside a calculator"></div>
  </section>
</main>

<footer class="abs footer">
  <nav class="abs footer-links">
    <span class="current">Home</span><span>Navigation</span><span>Directory</span><span>Special Offers</span><span>Contact Us</span>
    <span class="social"><span></span><span></span><span></span></span>
  </nav>
  <div class="abs legal">
    <span>© All Rights Reserved. Design by www.locatetaxpros.example</span><span>|</span><span>PO Box 4417</span><span>|</span><span>Ashford, CT</span><span>|</span><span>06999</span>
  </div>
  <div class="abs footer-brand"><span class="brand-dot"></span>LocateTaxPros</div>
</footer>
</body>
</html>
```